Corvalen Capital Modern Business Card

We need a modern business card template designed for Corvalen Capital.
Corvalen Capital is a diversified global cryptocurrency investment fund.

The font under the logo: Hiragino Kaku Gothic Pro

Color Hexcode: Main colors white (ffffff) & teal (188383), we are open to adding #fcca46 as an accent

Need time to get feedback from my team and to make sure designers better understand the brief.

Target Market(s)

Accredited Investors, high net worth individuals and institutional investors

Industry/Entity Type

Investment

Contact Information for Business Card

Contact Information should contain
Name
main phone +1 720 555 0147
cell
email

Font styles to use
Sans Serif
Other font styles liked:
• Hiragino Kaku Gothic Pro

Requirements
Must have
• would like to have icons that identify the contact information
• include our website: www.corvalencapital.example
• include our Tagline: Diversified Crypto Investment Funds
Nice to have
• Would like to have a simple back side with the logo (without the words) and plenty of space

```html
<!DOCTYPE html>
<html lang="en">
<head>
<meta charset="utf-8">
<title>Corvalen Capital – Business Card</title>
<link rel="stylesheet" href="https://fonts.googleapis.com/css2?family=Jost:wght@400;600&display=swap">
<style>
  :root {
    --teal: #229693;
    --teal-dark: #188383;
    --accent: #fecc4e;
    --paper: #ffffff;
    --page: #ffffff;
    --shadow: rgba(0, 0, 0, 0.16);
  }
  * { box-sizing: border-box; margin: 0; padding: 0; }
  html, body {
    width: 1200px;
    height: 848px;
    overflow: hidden;
    background: var(--page);
    font-family: "Jost", "Century Gothic", sans-serif;
  }
  .sheet {
    position: relative;
    width: 1200px;
    height: 848px;
  }
  .card {
    position: absolute;
    top: 256px;
    width: 524px;
    height: 338px;
    background: var(--paper);
    box-shadow: 0 5px 12px var(--shadow);
    overflow: hidden;
  }
  .card--front { left: 60px; }
  .card--back { left: 616px; }

  /* Front */
  .accent-block {
    position: absolute;
    left: 165px;
    top: 23px;
    width: 336px;
    height: 289px;
    background: var(--accent);
  }
  .brand {
    position: absolute;
    left: 37px;
    top: 196px;
  }
  .brand__lockup {
    display: flex;
    align-items: center;
    gap: 12px;
  }
  .brand__mark {
    width: 26px;
    height: 26px;
    background: var(--teal);
    flex: none;
  }
  .brand__name {
    font-size: 30px;
    font-weight: 600;
    line-height: 1;
    color: var(--teal);
    letter-spacing: 0.5px;
    white-space: nowrap;
  }
  .brand__tagline {
    margin-top: 12px;
    font-size: 14px;
    font-weight: 400;
    line-height: 1;
    color: var(--teal-dark);
    letter-spacing: 0.4px;
    white-space: nowrap;
  }

  /* Back */
  .accent-frame {
    position: absolute;
    left: 165px;
    top: 25px;
    width: 333px;
    height: 286px;
    border: 4px solid var(--accent);
  }
  .name-tag {
    position: absolute;
    left: 37px;
    top: 49px;
    width: 231px;
    height: 60px;
    background: var(--teal);
    color: var(--paper);
    padding: 5px 0 0 6px;
    line-height: 1;
  }
  .name-tag__name {
    display: block;
    font-size: 26px;
    font-weight: 600;
    letter-spacing: 0.3px;
  }
  .name-tag__role {
    display: block;
    margin-top: 3px;
    font-size: 19px;
    font-weight: 400;
    letter-spacing: 0.3px;
  }
  .contacts {
    position: absolute;
    left: 208px;
    top: 198px;
    list-style: none;
  }
  .contacts__item {
    display: flex;
    align-items: center;
    height: 23px;
    font-size: 15px;
    color: var(--teal);
    white-space: nowrap;
  }
  .contacts__icon {
    width: 16px;
    height: 16px;
    margin-right: 7px;
    fill: var(--teal);
    flex: none;
  }
</style>
</head>
<body>
<main class="sheet">
  <section class="card card--front" aria-label="Card front">
    <div class="accent-block"></div>
    <div class="brand">
      <div class="brand__lockup">
        <span class="brand__mark"></span>
        <span class="brand__name">Corvalen Capital</span>
      </div>
      <p class="brand__tagline">Diversified Crypto Investment Funds</p>
    </div>
  </section>

  <section class="card card--back" aria-label="Card back">
    <div class="accent-frame"></div>
    <div class="name-tag">
      <span class="name-tag__name">JOHN DOE</span>
      <span class="name-tag__role">GENERAL MANAGER</span>
    </div>
    <ul class="contacts">
      <li class="contacts__item">
        <svg class="contacts__icon" viewBox="0 0 16 16" aria-hidden="true">
          <path d="M1 5.5C1 3 4 2 8 2s7 1 7 3.5V7h-3.5V5.2h-7V7H1z"/>
          <path d="M3 8.5h10l1 5H2z"/>
        </svg>
        <span>+1 720 555 0147</span>
      </li>
      <li class="contacts__item">
        <svg class="contacts__icon" viewBox="0 0 16 16" aria-hidden="true">
          <path d="M4.5 1h7a1 1 0 0 1 1 1v12a1 1 0 0 1-1 1h-7a1 1 0 0 1-1-1V2a1 1 0 0 1 1-1zm.6 2v9h5.8V3zM8 12.6a.8.8 0 1 0 0 1.6.8.8 0 0 0 0-1.6z"/>
        </svg>
        <span>+1 720 555 0192</span>
      </li>
      <li class="contacts__item">
        <svg class="contacts__icon" viewBox="0 0 16 16" aria-hidden="true">
          <path d="M1 3h14v10H1zm1.6 1.5v.3L8 8.6l5.4-3.8v-.3zm0 2.1v4.9h10.8V6.6L8 10.4z"/>
        </svg>
        <span>contact@corvalencapital.example</span>
      </li>
      <li class="contacts__item">
        <svg class="contacts__icon" viewBox="0 0 16 16" aria-hidden="true">
          <path d="M8 1a7 7 0 1 0 0 14A7 7 0 0 0 8 1zm0 1.4c.7 0 1.6 1.5 1.9 4H6.1c.3-2.5 1.2-4 1.9-4zM5.9 2.8c-.6 1-1 2.3-1.1 3.6H2.5a5.6 5.6 0 0 1 3.4-3.6zm4.2 0a5.6 5.6 0 0 1 3.4 3.6h-2.3c-.1-1.3-.5-2.6-1.1-3.6zM2.5 7.8h2.3c.1 1.3.5 2.6 1.1 3.6a5.6 5.6 0 0 1-3.4-3.6zm3.6 0h3.8c-.3 2.5-1.2 4-1.9 4s-1.6-1.5-1.9-4zm5.1 0h2.3a5.6 5.6 0 0 1-3.4 3.6c.6-1 1-2.3 1.1-3.6z"/>
        </svg>
        <span>www.corvalencapital.example</span>
      </li>
    </ul>
  </section>
</main>
</body>
</html>
```